Consulting/ Manufacturers Representative Website

I need a website for a consulting/manufacturer representative company in Texas called Harbor Ledge Advisors. We Uncover and implement the right solution, at the right time, in the right way. We consult, we train, we offer project management, we offer performance improvement, we offer value creation, we turn stagnation into growth, and we offer corporate performance improvement.
I want the design to load on desktop and mobile, I want the site to look and feel professional like a large firm, and I want the site to be a marketing tool and establish a strong online presence.

Target Market(s)

City Governments, State Governments, County Governments, US Government, Power Plants, Refineries, Chemical Plants, Industrial customers

Industry/Entity Type

Consulting

Number of Pages Required

5+ page

Requirements
Must have
• mobile and desktop compatible, professional look, must be a fast website, company email and contact capabilities, contact page, company logo on website, SEO optimized, must display different industries served: Energy, Public (Government, Not For Profit, Educational), Transportation & Logistics, Business Services.
• Show that I help customers operate in a cleaner, safer and more economical way.
Nice to have
• news letter, news feed, show that company is principles based.
Should not have
• slow site, cheap look

```html
<!DOCTYPE html>
<html lang="en">
<head>
<meta charset="utf-8">
<title>Harbor Ledge Advisors</title>
<link rel="stylesheet" href="https://fonts.googleapis.com/css2?family=Montserrat:wght@400;500;600;700&family=Open+Sans:wght@400;600&display=swap">
<style>
:root{
  --green:#4aaf4c;
  --blue:#3494db;
  --dark:#242021;
  --ink:#1e1e1e;
  --muted:#666;
  --band:#f2f2f2;
  --white:#fff;
}
*{box-sizing:border-box;margin:0;padding:0}
html,body{width:1200px;height:3309px;overflow:hidden}
body{position:relative;background:var(--white);font-family:'Montserrat',sans-serif;color:var(--ink)}
.btn{position:absolute;display:flex;align-items:center;justify-content:center;background:var(--green);color:var(--white);font-family:'Montserrat',sans-serif;font-weight:600;font-size:13px;box-shadow:0 2px 4px rgba(0,0,0,.2)}

/* header */
.site-header{position:absolute;left:0;top:0;width:1200px;height:132px}
.brand{position:absolute;left:84px;top:22px;width:180px;display:flex;flex-direction:column;align-items:center;gap:8px}
.brand-mark{width:30px;height:30px;background:var(--ink)}
.brand-name{font-weight:700;font-size:14px;color:var(--ink);white-space:nowrap}
.nav-link{position:absolute;top:58px;font-size:13px;font-weight:600;color:var(--ink)}
.nav-link.active{color:var(--blue)}
.nav-active-bar{position:absolute;left:320px;top:0;width:88px;height:4px;background:var(--blue)}
.nav-call{position:absolute;left:797px;top:58px;font-size:13px;font-weight:600;color:var(--blue);display:flex;align-items:center;gap:6px}
.nav-cta{left:973px;top:48px;width:141px;height:36px;font-size:13px}

/* hero */
.hero{position:absolute;left:26px;top:132px;width:1145px;height:484px;background:linear-gradient(100deg,#7d6a5e 0%,#a8a29f 40%,#8e99a4 70%,#6f8aa3 100%)}
.hero-title{position:absolute;left:612px;top:162px;font-size:37px;font-weight:600;color:var(--white);line-height:44px}
.hero-sub{position:absolute;left:612px;top:262px;font-size:16px;color:var(--white);line-height:22px;font-family:'Open Sans',sans-serif}
.hero-dots{position:absolute;left:612px;top:404px;display:flex;gap:9px}
.hero-dots span{width:9px;height:9px;border-radius:50%;background:rgba(255,255,255,.75)}
.hero-dots span.on{background:var(--green)}

/* about */
.about-photo{position:absolute;left:110px;top:660px;width:308px;height:397px;background:linear-gradient(160deg,#b9c3cc 0%,#56606c 55%,#2c3440 100%)}
.about-title{position:absolute;left:471px;top:700px;font-size:24px;font-weight:600}
.about-lead{position:absolute;left:471px;top:752px;width:580px;font-family:'Open Sans',sans-serif;font-size:16px;line-height:23px;color:#555}
.about-body{position:absolute;left:471px;top:838px;width:580px;font-family:'Open Sans',sans-serif;font-size:12.5px;line-height:19px;color:#666}
.about-btn{left:471px;top:977px;width:141px;height:34px}

/* expertise */
.expertise{position:absolute;left:26px;top:1101px;width:1145px;height:545px;background:var(--band)}
.exp-title{position:absolute;left:108px;top:180px;font-size:25px;font-weight:600}
.exp-text{position:absolute;left:108px;top:230px;width:268px;font-family:'Open Sans',sans-serif;font-size:13px;line-height:20px;color:#666}
.exp-btn{left:108px;top:370px;width:141px;height:32px}
.exp-photo{position:absolute;left:419px;width:308px;height:220px}
.exp-photo.one{top:44px;background:linear-gradient(135deg,#e3e6ea 0%,#9aa4ae 50%,#4d5560 100%)}
.exp-photo.two{top:282px;background:linear-gradient(135deg,#8fa2b2 0%,#c9d2da 50%,#5d6770 100%)}
.exp-label{position:absolute;left:780px;font-size:12px;font-weight:600;color:var(--blue)}
.exp-copy{position:absolute;left:780px;width:260px;font-size:16px;font-weight:600;line-height:21px;color:var(--ink)}

/* industries */
.industries{position:absolute;left:26px;top:1647px;width:1145px;height:218px;display:flex}
.industry-tile{position:relative;width:286.25px;height:218px}
.industry-tile.gas{background:linear-gradient(180deg,#b49883,#6b5a4e)}
.industry-tile.city{background:linear-gradient(180deg,#c2ced8,#56697a)}
.industry-tile.solar{background:linear-gradient(180deg,#b28a5e,#2f3f58)}
.industry-tile.health{background:linear-gradient(180deg,#dfe3e6,#8a959e)}
.industry-tag{position:absolute;left:26px;top:118px;padding:3px 8px;background:var(--blue);color:var(--white);font-size:11px;font-weight:600}
.industry-name{position:absolute;left:26px;top:142px;width:240px;font-size:14px;font-weight:600;color:var(--white);line-height:20px}

/* why */
.why-title{position:absolute;left:0;top:1902px;width:1200px;text-align:center;font-size:25px;font-weight:600}
.why-sub{position:absolute;left:300px;top:1942px;width:600px;text-align:center;font-family:'Open Sans',sans-serif;font-size:13px;line-height:19px;color:#666}
.why-item{position:absolute;top:2010px;width:300px;text-align:center}
.why-item svg{display:block;margin:0 auto 18px}
.why-item p{font-size:14px;font-weight:500;line-height:21px}
.why-btn{left:529px;top:2160px;width:141px;height:34px}

/* insights */
.insights{position:absolute;left:26px;top:2239px;width:1145px;height:597px;background:var(--dark)}
.ins-title{position:absolute;left:108px;top:86px;font-size:24px;font-weight:600;color:var(--white)}
.ins-feature{position:absolute;left:108px;top:148px;width:560px;font-size:34px;font-weight:600;line-height:44px;color:var(--blue)}
.ins-meta{position:absolute;left:108px;top:402px;font-size:11px;font-weight:600;color:var(--white)}
.ins-btn{left:108px;top:473px;width:141px;height:34px}
.ins-card{position:absolute;left:754px;width:308px;height:156px;padding:34px 26px 0}
.ins-card.blue{background:var(--blue)}
.ins-card.green{background:var(--green)}
.ins-date{font-size:11px;font-weight:500;color:var(--ink);margin-bottom:12px}
.ins-text{font-size:14px;font-weight:600;line-height:21px;color:var(--white)}

/* contact strip */
.contact-head{position:absolute;top:2876px;font-size:14px;font-weight:600}
.contact-call{position:absolute;left:134px;top:2906px;font-size:22px;font-weight:500;color:var(--blue);display:flex;align-items:center;gap:8px}
.contact-mail{position:absolute;left:134px;top:2936px;font-size:13px;color:var(--blue)}
.news-input{position:absolute;left:471px;top:2912px;width:408px;height:34px;background:#f3f3f3;font-size:12px;color:#999;padding:10px 16px}
.news-btn{left:889px;top:2912px;width:172px;height:34px;box-shadow:none}

/* footer */
.site-footer{position:absolute;left:26px;top:2990px;width:1145px;height:291px;background:var(--band)}
.foot-col{position:absolute;top:44px;list-style:none}
.foot-col li{font-size:12px;line-height:25.5px;color:#555}
.foot-col li.current{color:var(--blue)}
.foot-copy{position:absolute;left:863px;top:48px;width:180px;font-size:12px;line-height:19px;color:#555}
.socials{position:absolute;left:863px;top:108px;display:flex;gap:8px}
.socials span{width:23px;height:23px}
</style>
</head>
<body>

<header class="site-header">
  <div class="brand"><span class="brand-mark"></span><span class="brand-name">Harbor Ledge Advisors</span></div>
  <div class="nav-active-bar"></div>
  <a class="nav-link active" style="left:330px">About Us</a>
  <a class="nav-link" style="left:427px">Expertise</a>
  <a class="nav-link" style="left:517px">industry</a>
  <a class="nav-link" style="left:605px">Insights</a>
  <a class="nav-link" style="left:685px">Contact Us</a>
  <div class="nav-call">Call:
    <svg width="12" height="12" viewBox="0 0 24 24"><path fill="currentColor" d="M6.6 10.8a15.1 15.1 0 0 0 6.6 6.6l2.2-2.2a1 1 0 0 1 1-.25 11.4 11.4 0 0 0 3.6.57 1 1 0 0 1 1 1V20a1 1 0 0 1-1 1A17 17 0 0 1 3 4a1 1 0 0 1 1-1h3.5a1 1 0 0 1 1 1c0 1.25.2 2.45.57 3.57a1 1 0 0 1-.25 1z"/></svg>
    512-555-0148</div>
  <a class="btn nav-cta">Consult Now!</a>
</header>

<section class="hero" role="img" aria-label="Photo of a team applauding in a bright office meeting">
  <h1 class="hero-title">We Uncover<br>and Implement</h1>
  <p class="hero-sub">the right solution, at the right<br>time, in the right way.</p>
  <div class="hero-dots"><span class="on"></span><span></span><span></span><span></span></div>
</section>

<section class="about">
  <div class="about-photo" role="img" aria-label="Photo of business people shaking hands, seen from below"></div>
  <h2 class="about-title">About Harbor Ledge Advisors</h2>
  <p class="about-lead">We are consulting/manufacturer representative company lorem ipsum dolor sit amet, consectetur adipiscing elit, Sed do eiusmod tempor incididunt ut labore et dolore magna aliqua.</p>
  <p class="about-body">Lorem ipsum dolor sit amet, consectetur adipiscing elit, sed do eiusmod tempor incididunt ut labore et dolore magna aliqua. Ut enim ad minim veniam, quis nostrud exercitation ullamco laboris nisi ut aliquip ex ea commodo consequat. Duis aute irure dolor in reprehenderit in voluptate velit esse cillum dolore eu fugiat nulla pariatur. Excepteur sint occaecat cupidatat non proident.</p>
  <a class="btn about-btn">About Us</a>
</section>

<section class="expertise">
  <h2 class="exp-title">Our Expertise</h2>
  <p class="exp-text">Or perhaps things are going well. Your company is growing quickly, and with that growth come challenges. You are faced with choices and opportunities.</p>
  <a class="btn exp-btn">Explore All</a>
  <div class="exp-photo one" role="img" aria-label="Photo of a trainer presenting at a whiteboard to a group"></div>
  <div class="exp-photo two" role="img" aria-label="Photo of colleagues discussing a project at a meeting table"></div>
  <div class="exp-label" style="top:84px">Consulting &amp; Training</div>
  <p class="exp-copy" style="top:106px">Lorem ipsum dolor sit amet, consectetur adipiscing elit, sed do eiusmod tempor incididunt ut labore et dolore magna aliqua. Ut enim ad minim veniam quis.</p>
  <div class="exp-label" style="top:322px">Project Management</div>
  <p class="exp-copy" style="top:344px">Lorem ipsum dolor sit amet, consectetur adipiscing elit, sed do eiusmod tempor incididunt ut labore et dolore magna aliqua. Ut enim ad minim veniam quis.</p>
</section>

<section class="industries">
  <div class="industry-tile gas" role="img" aria-label="Photo of a liquefied natural gas plant">
    <span class="industry-tag">Energy</span><p class="industry-name">Liquefied Natural<br>Gas Plant</p></div>
  <div class="industry-tile city" role="img" aria-label="Photo of glass office towers">
    <span class="industry-tag">Financial</span><p class="industry-name">City Vista of Houston<br>Lorem Ipsum</p></div>
  <div class="industry-tile solar" role="img" aria-label="Photo of industrial solar panels at sunset">
    <span class="industry-tag">Energy</span><p class="industry-name">Industrial Solar Panels and<br>Power Systems</p></div>
  <div class="industry-tile health" role="img" aria-label="Photo of a desk with medical paperwork">
    <span class="industry-tag">Health Care</span><p class="industry-name">Lorem Ipsum is simply<br>dummy text</p></div>
</section>

<section class="why">
  <h2 class="why-title">Why Harbor Ledge</h2>
  <p class="why-sub">Lorem ipsum dolor sit amet, consectetur adipiscing elit, sed do eiusmod tempor incididunt ut labore et dolore magna aliqua.</p>
  <div class="why-item" style="left:114px">
    <svg width="56" height="50" viewBox="0 0 56 50" fill="none" stroke="#4aaf4c" stroke-width="2.2"><circle cx="28" cy="8" r="5"/><path d="M28 13v10M10 23h36M10 23v8M28 23v8M46 23v8"/><circle cx="10" cy="36" r="4"/><circle cx="28" cy="36" r="4"/><circle cx="46" cy="36" r="4"/><path d="M3 48h50"/></svg>
    <p>Corporate Performance<br>Improvement</p></div>
  <div class="why-item" style="left:449px">
    <svg width="56" height="50" viewBox="0 0 56 50" fill="none" stroke="#4aaf4c" stroke-width="2.2"><path d="M19 4h4v5h4V4h2v5h4V4h4v10l-4 4v18l5 4v6H18v-6l5-4V18l-4-4z"/><path d="M23 18h10"/></svg>
    <p>Strategy and Value<br>Creation</p></div>
  <div class="why-item" style="left:784px">
    <svg width="60" height="50" viewBox="0 0 60 50" fill="none" stroke="#4aaf4c" stroke-width="2.2"><path d="M6 46V30a4 4 0 0 1 8 0v16M20 46V22a4 4 0 0 1 8 0v24M34 46V14a4 4 0 0 1 8 0v32M48 46V8a4 4 0 0 1 8 0v38M2 46h58"/></svg>
    <p>We Turn stagnation into<br>Growth</p></div>
  <a class="btn why-btn">Contact Us</a>
</section>

<section class="insights">
  <h2 class="ins-title">Latest Insights</h2>
  <p class="ins-feature">Lorem ipsum dolor sit amet, consectetur adipiscing elit, sed do eiusmod tempor incid-idunt ut labore et dolore magna aliqua.</p>
  <div class="ins-meta">17 Mar. 2018 &nbsp;|&nbsp; Business Insights</div>
  <a class="btn ins-btn">View All</a>
  <article class="ins-card blue" style="top:44px"><div class="ins-date">17 Mar. 2018</div><p class="ins-text">Lorem ipsum dolor sit amet, consectetur adipiscing elit, sed do eiusmod tempor...</p></article>
  <article class="ins-card green" style="top:220px"><div class="ins-date">17 Mar. 2018</div><p class="ins-text">Lorem ipsum dolor sit amet, consectetur adipiscing elit, sed do eiusmod tempor...</p></article>
  <article class="ins-card blue" style="top:396px"><div class="ins-date">17 Mar. 2018</div><p class="ins-text">Lorem ipsum dolor sit amet, consectetur adipiscing elit, sed do eiusmod tempor...</p></article>
</section>

<section class="contact-strip">
  <h3 class="contact-head" style="left:134px">Get in Touch</h3>
  <div class="contact-call">CALL:
    <svg width="18" height="18" viewBox="0 0 24 24"><path fill="currentColor" d="M6.6 10.8a15.1 15.1 0 0 0 6.6 6.6l2.2-2.2a1 1 0 0 1 1-.25 11.4 11.4 0 0 0 3.6.57 1 1 0 0 1 1 1V20a1 1 0 0 1-1 1A17 17 0 0 1 3 4a1 1 0 0 1 1-1h3.5a1 1 0 0 1 1 1c0 1.25.2 2.45.57 3.57a1 1 0 0 1-.25 1z"/></svg>
    512-555-0148</div>
  <div class="contact-mail">E. hello@harborledge.example</div>
  <h3 class="contact-head" style="left:471px">Sign Up Newsletter</h3>
  <div class="news-input">Enter Your Email</div>
  <a class="btn news-btn">SIGN UP NOW!</a>
</section>

<footer class="site-footer">
  <ul class="foot-col" style="left:108px">
    <li class="current">Home</li><li>About Harbor Ledge</li><li>Expertise</li><li>Insights</li><li>Industry</li><li>Our People</li><li>Contact</li>
  </ul>
  <ul class="foot-col" style="left:361px">
    <li>Global Locations</li><li>Careers</li><li>Alumni</li><li>Contact Us</li>
  </ul>
  <ul class="foot-col" style="left:614px">
    <li>Quillmere Vantage Capital</li><li>Quillmere Vantage Real Estate</li><li>Employee Portal</li><li>Privacy Policy</li><li>Terms of Use</li>
  </ul>
  <p class="foot-copy">©2018 Harbor Ledge Advisors.</p>
  <div class="socials">
    <span style="background:#3b5998"></span><span style="background:#38a9e6"></span><span style="background:#444"></span><span style="background:#e0321c"></span>
  </div>
</footer>

</body>
</html>
```